Billboard design 8x3M LUMA (Spanish company)

We´re located in the south of Spain. We run a local telecom company.
We sell Fiber optic, and mobile phone lines mainly.
The billboard will have to be in Spanish, I would like the price to be something you spot on first sight when passing by in the car.
Our company color is blue, like in our logo which I will add. I will also add a example from what we currently have.
The new offer should be:
1000 megas + 100Gigas movil con llamadas ilimitadas. (meaning 1000Mb fiber optic speed and 100Gb data and unlimited calls for 1 mobile line)
Our details are: phone line 956 47 8092
Website: lu-ma.es

```html
<!DOCTYPE html>
<html lang="es">
<head>
<meta charset="utf-8">
<title>LUMA – Valla 8x3</title>
<link rel="stylesheet" href="https://fonts.googleapis.com/css2?family=Montserrat:wght@500;600;700;800&display=swap">
<style>
  :root {
    --stage: #e8edf0;
    --blue-light: #1f86b8;
    --blue-dark: #0d5f8a;
    --yellow: #eef03a;
    --white: #ffffff;
    --photo-dark: #1c262b;
    --photo-warm: #5a3a22;
  }
  * { margin: 0; padding: 0; box-sizing: border-box; }
  html, body { width: 1200px; height: 1200px; overflow: hidden; }
  body {
    background: var(--stage);
    font-family: "Montserrat", Arial, sans-serif;
    color: var(--white);
    display: flex; align-items: center; justify-content: center;
  }
  .billboard {
    position: relative;
    width: 1200px; height: 450px;
    background: linear-gradient(100deg, var(--blue-light) 0%, #1677a8 45%, var(--blue-dark) 100%);
    overflow: hidden;
  }
  .imagery { position: absolute; inset: 0; }
  .brand { position: absolute; left: 56px; top: 92px; }
  .brand-name {
    font-weight: 800; font-size: 64px; letter-spacing: 4px; line-height: 1;
    display: flex; align-items: center; gap: 12px;
  }
  .brand-dot { width: 16px; height: 16px; border-radius: 50%; background: var(--white); }
  .brand-services { font-weight: 600; font-size: 17px; margin-top: 10px; letter-spacing: 0.3px; }
  .tagline {
    position: absolute; left: 56px; top: 248px;
    font-weight: 700; font-size: 25px; line-height: 1.3; text-transform: uppercase;
  }
  .legal { position: absolute; left: 56px; top: 408px; font-weight: 600; font-size: 11px; }
  .contact { position: absolute; left: 505px; top: 318px; font-weight: 700; }
  .contact-phone { display: flex; align-items: center; gap: 14px; font-size: 36px; }
  .contact-web { font-size: 33px; margin-top: 6px; }
  .offer { position: absolute; left: 808px; top: 92px; }
  .offer-speed { color: var(--yellow); font-weight: 800; font-size: 92px; line-height: 1; letter-spacing: -1px; }
  .offer-speed small { font-size: 54px; letter-spacing: 0; }
  .offer-data { font-weight: 800; font-size: 58px; line-height: 1; margin-top: 14px; padding-left: 36px; }
  .offer-mobile {
    display: flex; align-items: center; gap: 16px;
    font-weight: 800; font-size: 62px; line-height: 1; margin-top: 14px; padding-left: 66px;
  }
  .offer-calls { font-weight: 600; font-size: 23px; line-height: 1.3; margin-top: 12px; padding-left: 128px; }
</style>
</head>
<body>
  <main class="billboard">
    <svg class="imagery" width="1200" height="450" viewBox="0 0 1200 450">
      <defs>
        <linearGradient id="laptopShade" x1="0" y1="0" x2="1" y2="1">
          <stop offset="0" stop-color="#24343a"/>
          <stop offset="0.6" stop-color="var(--photo-dark)"/>
          <stop offset="1" stop-color="#4a3322"/>
        </linearGradient>
        <linearGradient id="deskShade" x1="0" y1="0" x2="1" y2="1">
          <stop offset="0" stop-color="#1f3a36"/>
          <stop offset="1" stop-color="var(--photo-warm)"/>
        </linearGradient>
      </defs>
      <path class="photo-main" role="img" aria-label="Foto: manos escribiendo en un portátil con pantalla de carga"
            d="M270 0 H810 L528 282 Q505 305 482 282 Z" fill="url(#laptopShade)"/>
      <rect class="photo-small" role="img" aria-label="Foto: persona con portátil sobre mesa de madera"
            x="230" y="270" width="170" height="170" rx="18"
            transform="rotate(45 315 355)" fill="url(#deskShade)"/>
      <g class="wifi-icon" fill="none" stroke="var(--yellow)" stroke-width="7" stroke-linecap="round">
        <path d="M540 62 a46 46 0 0 1 62 0"/>
        <path d="M552 76 a28 28 0 0 1 38 0"/>
        <circle cx="571" cy="92" r="5" fill="var(--yellow)" stroke="none"/>
      </g>
    </svg>

    <div class="brand">
      <div class="brand-name"><span class="brand-dot"></span>LUMA</div>
      <div class="brand-services">Wifi | Fibra | Movil | Tv</div>
    </div>

    <p class="tagline">Tu fibra + móvil<br>al mejor precio</p>
    <p class="legal">*Consulte condiciones</p>

    <div class="contact">
      <div class="contact-phone">
        <svg width="20" height="32" viewBox="0 0 20 32" aria-hidden="true">
          <rect x="2" y="2" width="16" height="28" rx="3" fill="none" stroke="var(--yellow)" stroke-width="3"/>
          <line x1="8" y1="25" x2="12" y2="25" stroke="var(--yellow)" stroke-width="2.5" stroke-linecap="round"/>
        </svg>
        <span>956 47 8092</span>
      </div>
      <div class="contact-web">www.lu-ma.es</div>
    </div>

    <div class="offer">
      <div class="offer-speed">1000<small>mb</small></div>
      <div class="offer-data">+ 100 Gb</div>
      <div class="offer-mobile">
        <svg width="30" height="50" viewBox="0 0 30 50" aria-hidden="true">
          <rect x="3" y="3" width="24" height="44" rx="4" fill="none" stroke="var(--yellow)" stroke-width="4"/>
          <line x1="12" y1="40" x2="18" y2="40" stroke="var(--yellow)" stroke-width="3" stroke-linecap="round"/>
        </svg>
        <span>móvil</span>
      </div>
      <div class="offer-calls">con llamadas<br>ilimitadas</div>
    </div>
  </main>
</body>
</html>
```